Web Design for an Employment Agency

We need a website design for an employment agency here in New Zealand.

We have attached a few examples of what other designers have submitted but the client is not exactly happy with the concepts and what came out in the end.

They have given this link for some idea of the sketches look they like: http://www.quillbrookgallery.com/artist-fuses-animals-with-nature-pen-sketches/

They have asked to use "maori sketches" in black and white through the website, you can Google "Maori art" or "Maori drawings" to get an idea of the type of drawings that they are.

Please ensure the concept designs incorporate some sort of those maori designs through out the website.

Unfortunately we do not have a lot of copy to work with, but please use filler text and content for areas if need be and we can get extra copy from the client afterwards.

The client does not want people or buildings

Also, the logo should be displayed as it is currently – they do not want to deviate from it.

They also would like Maori type of sketches (in Black and white) the grey colour can be used as a background when you use the logo on the page.

The design must be professional and bold.

The service they offer is all about professionalism.

------------------------------------------------------------------
UPDATE - 20th FEBRUARY

Please see attached file for the brief of the different sections of the website as well as some examples of the maori designs from framelodger.

I have also attached another design she liked the look of the most, but se wanted the following changes made to it:

- She does not want the photo at the top with the hand writing, she wants her logo in a watermark format to show there in the background
- She wants where you have those other images in circle, she wants "maori" type designs to be incorporated somewhere there
- She needs the content that we have provided to be all there on the page in the different sections, I will re-send you the content

Please re-submit your concepts based along the lines of that, please ensure the text and content match the sections and I will send to her for final approval.

Updates

Looking for designs to come through ASAP please

Target Market(s)

New Zealand people looking for jobs, and people looking for workers in NZ

Industry/Entity Type

Employment Agency

Number of Pages Required

4 page

Font styles to use
Sans Serif

Colors

Designer to choose colors to be used in the design.

Requirements
Must have
• It needs to be nice and clean perhaps grey scale like the attached
• The design must be professional and bold.
• They also would like Maori type of sketches (in Black and white) the grey colour can be used as a background when you use the logo on the page.
Nice to have
• You can think about the business, maybe do some of the copy or content as well to make more attractive to the client when I show them
Should not have
• Do not have lots of colour, The client does not want people or buildings

```html
<!DOCTYPE html>
<html lang="en">
<head>
<meta charset="utf-8">
<title>Kaimahi.net – Employment Agency</title>
<link href="https://fonts.googleapis.com/css2?family=Hind:wght@400;500;600&display=swap" rel="stylesheet">
<style>
:root{
  --stage:#e4e4e4;
  --paper:#f7f7f7;
  --footer:#f0f0f0;
  --charcoal:#444444;
  --ink:#333333;
  --muted:#8a8a8a;
  --pale:#dcdcdc;
  --white:#ffffff;
}
*{margin:0;padding:0;box-sizing:border-box}
html,body{width:1200px;height:1200px;overflow:hidden;background:var(--stage);font-family:"Hind",Arial,sans-serif;color:var(--ink)}
.site{position:absolute;left:84px;top:0;width:1004px;height:1167px;transform:scale(1.028);transform-origin:0 0;overflow:hidden}
.services{position:absolute;left:0;top:0;width:1004px;height:408px;background:var(--paper);overflow:hidden}
.faint-pattern{position:absolute;border-radius:50%}
.services .faint-pattern{left:21px;top:-120px;width:540px;height:540px;background:radial-gradient(circle,#f1f1f1 0%,#ececec 70%,#efefef 100%)}
.feature-art{position:absolute;left:560px;top:-146px;width:328px;height:328px;border-radius:50%;background:radial-gradient(circle at 50% 60%,#6a6a6a 0%,#3a3a3a 55%,#2a2a2a 100%)}
.service{position:absolute;left:137px}
.service .icon{position:absolute;left:0;top:0}
.service h3{position:absolute;left:71px;top:0;width:300px;font-size:16px;font-weight:500;line-height:20px;color:var(--ink)}
.service p{position:absolute;left:71px;top:30px;width:290px;font-size:10.5px;line-height:17px;color:var(--muted)}
.consult{position:absolute;left:140px;top:292px;width:350px;height:63px;background:#f3f3f3;padding:15px 24px;font-size:10.5px;line-height:17px;color:var(--muted)}
.testimonials{position:absolute;left:0;top:408px;width:1004px;height:452px;background:var(--charcoal);overflow:hidden}
.testimonials .faint-pattern{left:240px;top:112px;width:524px;height:524px;background:radial-gradient(circle,#4a4a4a 0%,#474747 70%,#464646 100%)}
.testimonials h2{position:absolute;left:0;width:1004px;top:62px;text-align:center;font-size:26px;font-weight:600;color:var(--white)}
.arrow{position:absolute;top:178px}
.avatar{position:absolute;left:289px;top:161px;width:86px;height:86px;border-radius:50%;border:3px solid var(--white);background:radial-gradient(circle at 50% 40%,#d9b59a 0%,#a07a5c 55%,#6f8a9c 100%)}
.quote{position:absolute;left:410px;top:163px;width:312px;font-size:10.5px;line-height:18px;color:#e2e2e2}
.author{position:absolute;left:410px;top:272px;font-size:17px;font-weight:400;letter-spacing:.4px;color:var(--white)}
.place{position:absolute;left:410px;top:298px;font-size:10.5px;color:#a0a0a0}
.dots{position:absolute;left:456px;top:385px;display:flex;gap:18px}
.dots span{width:10px;height:10px;border-radius:50%;background:#bdbdbd}
.dots span.active{background:var(--white)}
.footer{position:absolute;left:0;top:860px;width:1004px;height:307px;background:var(--footer)}
.footer h4{position:absolute;top:54px;font-size:10.5px;font-weight:500;letter-spacing:.8px;color:var(--ink)}
.field{position:absolute;left:200px;width:210px;background:var(--white);border:1px solid #e6e6e6;font-size:9.5px;color:#999;padding:9px 13px}
.submit{position:absolute;left:200px;top:222px;width:210px;height:34px;background:var(--charcoal);color:var(--white);font-size:10.5px;font-weight:600;letter-spacing:.5px;text-align:center;line-height:35px}
.contact-row{position:absolute;left:488px;display:flex;align-items:center;gap:10px;font-size:10.5px;font-weight:500;color:var(--ink)}
.contact-row svg{width:16px;height:16px}
.social{position:absolute;left:715px;top:88px;display:flex;gap:14px}
.social span{width:22px;height:22px;border-radius:50%;background:var(--ink)}
.brand{position:absolute;left:722px;top:208px;display:flex;align-items:center;gap:7px;font-size:13px;font-weight:500;color:var(--ink)}
.brand i{width:12px;height:12px;border-radius:50%;border:1.5px solid var(--ink)}
</style>
</head>
<body>
<main class="site">

  <section class="services">
    <div class="faint-pattern" role="img" aria-label="Faint Maori pattern circle in the background"></div>
    <div class="feature-art" role="img" aria-label="Black and white Maori pattern medallion"></div>

    <div class="service" style="top:5px">
      <svg class="icon" width="50" height="40" viewBox="0 0 50 40" style="top:-4px">
        <path d="M4 13h10l22-11v34L14 25H4z" fill="#333"/>
        <rect x="8" y="25" width="7" height="12" fill="#333"/>
        <rect x="40" y="12" width="5" height="14" rx="2" fill="#333"/>
      </svg>
      <h3>Marketing the candidate</h3>
      <p>Presenting you to Companies seeking your skills and matching the Employers requirements to your field of Expertise (Career Hunting for positions in the market and initial representation at the Employer)</p>
    </div>

    <div class="service" style="top:127px">
      <svg class="icon" width="48" height="50" viewBox="0 0 48 50" style="top:-6px">
        <circle cx="24" cy="21" r="14" fill="#333"/>
        <rect x="17" y="33" width="14" height="7" fill="#333"/>
        <path d="M20 42h8l-4 5z" fill="#333"/>
        <path d="M26 12l-7 11h5l-2 8 7-11h-5z" fill="#fff"/>
        <g fill="#333"><circle cx="3" cy="21" r="1.5"/><circle cx="45" cy="21" r="1.5"/><circle cx="9" cy="6" r="1.5"/><circle cx="39" cy="6" r="1.5"/><circle cx="24" cy="1.5" r="1.5"/></g>
      </svg>
      <h3>Self-listing suggestions<br>– positions available</h3>
    </div>

    <div class="service" style="top:205px">
      <svg class="icon" width="50" height="48" viewBox="0 0 50 48" style="left:3px;top:-8px">
        <rect x="0" y="0" width="36" height="40" rx="3" fill="#333"/>
        <g fill="#fff"><rect x="7" y="9" width="22" height="3"/><rect x="7" y="17" width="22" height="3"/><rect x="7" y="25" width="14" height="3"/></g>
        <path d="M26 30l4-4 15 15-4 4z" fill="#333" stroke="#f7f7f7" stroke-width="2"/>
      </svg>
      <h3>2 Written references done</h3>
    </div>

    <div class="consult">The first Consultation is free so give us a call or drop us a mail to find the best solution for you</div>
  </section>

  <section class="testimonials">
    <div class="faint-pattern" role="img" aria-label="Faint Maori koru pattern circle in the background"></div>
    <h2>Testimonials</h2>
    <svg class="arrow" style="left:128px" width="26" height="44" viewBox="0 0 26 44"><path d="M22 2L4 22l18 20" fill="none" stroke="#5c5c5c" stroke-width="3"/></svg>
    <svg class="arrow" style="left:850px" width="26" height="44" viewBox="0 0 26 44"><path d="M4 2l18 20L4 42" fill="none" stroke="#5c5c5c" stroke-width="3"/></svg>
    <div class="avatar" role="img" aria-label="Portrait photo of the client giving the testimonial"></div>
    <p class="quote">Lorem ipsum dolor sit amet, consectetur adipiing elitsed do eiusmod tempor incididunt ut labore et dolore magna aliqua. Ut enim ad minim veniamq uis nostrud exercitation ullamco laboris nisi utliqux ea commodo consequat. Duis aute irure dolor in reprehenderit</p>
    <p class="author">Mere Hollis</p>
    <p class="place">Auckland</p>
    <div class="dots"><span class="active"></span><span></span><span></span><span></span></div>
  </section>

  <footer class="footer">
    <h4 style="left:200px">GET IN TOUCH</h4>
    <h4 style="left:490px">CONTACT US</h4>
    <h4 style="left:716px">SOCIAL MEDIA</h4>

    <div class="field" style="top:87px;height:30px">Full Name</div>
    <div class="field" style="top:123px;height:30px">Email Address</div>
    <div class="field" style="top:159px;height:57px">Message...</div>
    <div class="submit">SUBMIT</div>

    <div class="contact-row" style="top:88px">
      <svg viewBox="0 0 16 16"><path d="M8 1a5 5 0 0 0-5 5c0 4 5 9 5 9s5-5 5-9a5 5 0 0 0-5-5z" fill="#333"/><circle cx="8" cy="6" r="1.8" fill="#f0f0f0"/></svg>
      <span>Riverside, Auckland</span>
    </div>
    <div class="contact-row" style="top:123px">
      <svg viewBox="0 0 16 16"><rect x="4" y="1" width="8" height="14" rx="1" fill="#333"/><rect x="5.5" y="3" width="5" height="4" fill="#f0f0f0"/><g fill="#f0f0f0"><rect x="5.5" y="9" width="1.5" height="1.5"/><rect x="9" y="9" width="1.5" height="1.5"/><rect x="5.5" y="12" width="1.5" height="1.5"/><rect x="9" y="12" width="1.5" height="1.5"/></g></svg>
      <span>+64 81 000 52837</span>
    </div>
    <div class="contact-row" style="top:158px">
      <svg viewBox="0 0 16 16"><circle cx="8" cy="8" r="2.6" fill="none" stroke="#333" stroke-width="1.8"/><path d="M10.6 8v1.3a1.8 1.8 0 0 0 3.6 0V8A6.2 6.2 0 1 0 11 13.3" fill="none" stroke="#333" stroke-width="1.8"/></svg>
      <span>aroha@kaimahi.net</span>
    </div>

    <div class="social" aria-label="Social media links"><span></span><span></span><span></span></div>

    <div class="brand"><i></i>Kaimahi.net</div>
  </footer>

</main>
</body>
</html>
```